business card design for a plumbing contractor

i need a double business card for a plumbing business, our initial service is residential Sewer Drain Cleaning.

Target Market(s)

other plumbing Business

Industry/Entity Type

Plumbing

Contact Information for Business Card

www.PipeworksTopNotch.example- 5173829046-

Font styles to use
Serif

Colors
ec1f27
0455a3

```html
<!DOCTYPE html>
<html lang="en">
<head>
<meta charset="utf-8">
<title>Pipeworks Top Notch – Business Card</title>
<link rel="stylesheet" href="https://fonts.googleapis.com/css2?family=Ubuntu:wght@400;500;700&display=swap">
<style>
  :root {
    --brand-blue: #0455a3;
    --card-blue: #2b64a0;
    --deep-blue: #1c4f8c;
    --brand-red: #ec1f27;
    --dark-red: #b3141b;
    --paper: #ffffff;
    --paper-shade: #e9e9ea;
    --logo-grey: #6b6560;
    --backdrop: #d9dbde;
  }
  * { box-sizing: border-box; margin: 0; padding: 0; }
  html, body {
    width: 1200px; height: 997px; overflow: hidden;
    background: var(--backdrop);
    font-family: "Ubuntu", "Helvetica Neue", Arial, sans-serif;
  }
  .canvas {
    position: relative; width: 1200px; height: 997px;
  }
  .card {
    position: absolute; left: 250px; width: 700px; height: 400px;
    border-radius: 26px; overflow: hidden;
    box-shadow: 0 10px 30px rgba(0,0,0,.25);
  }
  /* ---------- front ---------- */
  .card-front {
    top: 60px;
    background: linear-gradient(160deg, #3473b3 0%, var(--card-blue) 55%, #245a94 100%);
  }
  .card-front .wordmark {
    position: absolute; left: 0; right: 0; top: 120px;
    text-align: center; color: var(--paper);
    font-weight: 700; font-size: 64px; line-height: 1; letter-spacing: .5px;
  }
  .card-front .tagline-band {
    position: absolute; left: 0; right: 0; top: 318px; height: 30px;
    background: var(--brand-red);
    border-top: 2px solid var(--dark-red); border-bottom: 2px solid var(--dark-red);
    color: var(--paper); font-size: 13px; letter-spacing: 1.2px;
    display: flex; align-items: center; justify-content: center;
    text-transform: uppercase;
  }
  /* ---------- back ---------- */
  .card-back {
    top: 537px;
    background: var(--paper);
  }
  .card-back .backdrop-shapes {
    position: absolute; inset: 0;
  }
  .card-back .wordmark {
    position: absolute; left: 0; right: 0; top: 92px;
    text-align: center; color: var(--logo-grey);
    font-weight: 700; font-size: 48px; line-height: 1;
  }
  .card-back .person {
    position: absolute; left: 0; right: 0; top: 206px;
    text-align: center; color: var(--paper);
  }
  .person-name { font-size: 22px; font-weight: 700; letter-spacing: 1px; text-transform: uppercase; }
  .person-role { font-size: 14px; font-weight: 500; margin-top: 2px; }
  .contact-list {
    position: absolute; left: 40px; top: 290px; list-style: none;
    color: var(--paper); font-size: 17px;
  }
  .contact-list li { display: flex; align-items: center; gap: 12px; height: 32px; }
  .contact-icon {
    width: 20px; height: 20px; border-radius: 50%;
    background: var(--brand-red); display: flex; align-items: center; justify-content: center;
    flex: none;
  }
  .contact-icon svg { width: 12px; height: 12px; }
  .faint-mark {
    position: absolute; right: 70px; top: 250px; width: 110px; height: 110px;
    border-radius: 50%; background: rgba(255,255,255,.12);
  }
</style>
</head>
<body>
<main class="canvas">

  <section class="card card-front" aria-label="Business card front">
    <div class="wordmark">Pipeworks Top Notch</div>
    <div class="tagline-band">Sewer drain cleaning, maintenance, trenchless pipe installs</div>
  </section>

  <section class="card card-back" aria-label="Business card back">
    <svg class="backdrop-shapes" viewBox="0 0 700 400" preserveAspectRatio="none" aria-hidden="true">
      <defs>
        <linearGradient id="paperShade" x1="0" y1="0" x2="0" y2="1">
          <stop offset="0" stop-color="#ffffff"/>
          <stop offset="1" stop-color="#e4e4e6"/>
        </linearGradient>
      </defs>
      <rect width="700" height="400" fill="url(#paperShade)"/>
      <polygon points="0,215 170,185 530,185 700,150 700,400 0,400" fill="var(--deep-blue)"/>
      <polygon points="0,205 0,220 170,195 170,185" fill="var(--dark-red)"/>
      <polygon points="530,185 700,150 700,162 530,196" fill="var(--dark-red)"/>
      <polygon points="185,185 515,185 540,198 515,262 185,262 160,198" fill="var(--brand-red)"/>
      <polygon points="160,198 185,262 160,250" fill="var(--dark-red)"/>
      <polygon points="540,198 515,262 540,250" fill="var(--dark-red)"/>
    </svg>
    <div class="wordmark">Pipeworks Top Notch</div>
    <div class="person">
      <div class="person-name">Dana Merrick</div>
      <div class="person-role">Personal Trainer</div>
    </div>
    <div class="faint-mark" aria-hidden="true"></div>
    <ul class="contact-list">
      <li>
        <span class="contact-icon"><svg viewBox="0 0 12 12"><path d="M3 1.5 4.6 3.4 3.8 4.6c.6 1.3 1.9 2.6 3.6 3.6l1.2-.8 1.9 1.6-1 1.4C5.5 10.2 1.8 6.5 1.6 2.5z" fill="#fff"/></svg></span>
        <span>5173829046</span>
      </li>
      <li>
        <span class="contact-icon"><svg viewBox="0 0 12 12"><rect x="1.5" y="3" width="9" height="6" fill="none" stroke="#fff" stroke-width="1.2"/><path d="M1.5 3 6 6.6 10.5 3" fill="none" stroke="#fff" stroke-width="1.2"/></svg></span>
        <span>Dispatcher@PipeworksTopNotch.example</span>
      </li>
      <li>
        <span class="contact-icon"><svg viewBox="0 0 12 12"><circle cx="6" cy="6" r="4.2" fill="none" stroke="#fff" stroke-width="1.1"/><path d="M1.8 6h8.4M6 1.8c-2 2.4-2 6 0 8.4M6 1.8c2 2.4 2 6 0 8.4" fill="none" stroke="#fff" stroke-width=".9"/></svg></span>
        <span>www.PipeworksTopNotch.example</span>
      </li>
    </ul>
  </section>

</main>
</body>
</html>
```